Fennel Cellar Online organic artisan and gourmet supermarket

Brief:
Brand: Fennel Cellar (FC) is an online store selling artisan and organinc Italian products. Our look and feel we have gone with is rustic, premium and unfiltered (visit us @ www.fennelcellar.com.au)
Our slogan: "cook Italy, eat Italy, love Italy"
Goals: prior to our online store going live, we used to attend a food market once a week. Due to unfortunate circumstances, we stopped. Since then, our store has gone live and wanted to use the card as a reminder we are back at the markets.
I also have a restaurant, "fennel ristorante" so I wanted to hand them out to customers in the restaurant but also act as reminder of our pop up market stores and our website to buy from.
Personality: FC is more than just a store. Our goal is to be not only a store but an informationa hub of Italian food.
We offer assistance to people who need help in their kitchen as well as catering
Logo: I have a logo which I was not able to upload.

Target Market(s)

Food lovers
Italian food interest
Wealthy
Organic gourmet food enthusiest

Industry/Entity Type

Store

Contact Information for Business Card

Shop online or visit us @ Willow Bend organic market
Ciao@fennelcellar.com.au
Www.fennelcellar.com.au

Online store, Cooking advice, catering, ristorante and information hub

Requirements
Must have
• Logo
• Information
• May be larger than a business card to fit information but smaller than a post card
• Need to look interesting and different
• Not a simple card design
Nice to have
• Different fonts
• Rustic looking
• Qwerky

```html
<!DOCTYPE html>
<html lang="en">
<head>
<meta charset="utf-8">
<title>Fennel Cellar – Business Card</title>
<link rel="stylesheet" href="https://fonts.googleapis.com/css2?family=Open+Sans:wght@400;600;700&display=swap">
<style>
  :root {
    --stage: #eeeae6;
    --card-red: #cc0022;
    --card-white: #ffffff;
    --ink-light: #ffffff;
    --ink-dark: #1a1a1a;
    --accent-red: #cc0022;
  }
  html, body {
    margin: 0;
    padding: 0;
    width: 1200px;
    height: 900px;
    overflow: hidden;
    background: var(--stage);
    font-family: "Open Sans", Arial, sans-serif;
  }
  .canvas {
    position: relative;
    width: 1200px;
    height: 900px;
  }
  .card {
    position: absolute;
    box-shadow: 0 6px 18px rgba(0,0,0,0.12);
  }
  /* Front: red card, rounded right side */
  .card--front {
    left: 238px;
    top: 60px;
    width: 555px;
    height: 345px;
    background: var(--card-red);
    color: var(--ink-light);
    border-radius: 0 175px 175px 0;
  }
  .person {
    position: absolute;
    left: 39px;
    top: 114px;
  }
  .person__name {
    margin: 0;
    font-size: 18px;
    font-weight: 700;
    line-height: 1.2;
  }
  .person__role {
    margin: 0;
    font-size: 15px;
    font-weight: 400;
    line-height: 1.3;
  }
  .contact {
    position: absolute;
    left: 39px;
    top: 175px;
    margin: 0;
    padding: 0;
    list-style: none;
    font-size: 15px;
    line-height: 21px;
  }
  .contact__item {
    display: flex;
    align-items: center;
    gap: 10px;
  }
  .contact__icon {
    width: 11px;
    height: 11px;
    flex: none;
  }
  .slogan {
    position: absolute;
    left: 39px;
    top: 245px;
    margin: 0;
    font-size: 15px;
  }
  .market {
    position: absolute;
    left: 42px;
    top: 278px;
    margin: 0;
    font-size: 15px;
    font-weight: 600;
  }
  .brand-mark {
    position: absolute;
    display: flex;
    align-items: center;
    gap: 10px;
    white-space: nowrap;
  }
  .brand-mark__dot {
    border-radius: 50%;
    flex: none;
  }
  .card--front .brand-mark {
    left: 330px;
    top: 152px;
    font-size: 22px;
    font-weight: 600;
    color: var(--ink-light);
  }
  .card--front .brand-mark__dot {
    width: 14px;
    height: 14px;
    background: var(--ink-light);
  }
  /* Back: white card, rounded left side */
  .card--back {
    left: 460px;
    top: 518px;
    width: 558px;
    height: 342px;
    background: var(--card-white);
    border-radius: 171px 0 0 171px;
  }
  .card--back .brand-mark {
    left: 50px;
    top: 154px;
    font-size: 26px;
    font-weight: 600;
    color: var(--ink-dark);
  }
  .card--back .brand-mark__dot {
    width: 16px;
    height: 16px;
    background: var(--ink-dark);
  }
  .services {
    position: absolute;
    right: 40px;
    top: 98px;
    margin: 0;
    padding: 0;
    list-style: none;
    text-align: right;
    color: var(--accent-red);
    font-size: 15px;
    font-weight: 600;
    line-height: 31px;
  }
</style>
</head>
<body>
<main class="canvas">
  <section class="card card--front" aria-label="Card front">
    <div class="person">
      <p class="person__name">Marco Bellini</p>
      <p class="person__role">Managing Director</p>
    </div>
    <ul class="contact">
      <li class="contact__item">
        <svg class="contact__icon" viewBox="0 0 12 12" aria-hidden="true">
          <rect x="1" y="2.5" width="10" height="7" fill="#fff"/>
          <path d="M1 2.5 L6 6.5 L11 2.5" fill="none" stroke="#cc0022" stroke-width="1"/>
        </svg>
        <span>Ciao@fennelcellar.com.au</span>
      </li>
      <li class="contact__item">
        <svg class="contact__icon" viewBox="0 0 12 12" aria-hidden="true">
          <circle cx="6" cy="6" r="5.5" fill="#fff"/>
          <path d="M3 4 Q5 3 6 5 T9 7 M4 8 Q5 9 7 9" fill="none" stroke="#cc0022" stroke-width="1"/>
        </svg>
        <span>Www.fennelcellar.com.au</span>
      </li>
    </ul>
    <p class="slogan">"cook Italy, eat Italy, love Italy"</p>
    <p class="market">Shop online or visit us @ Willow Bend organic market</p>
    <div class="brand-mark">
      <span class="brand-mark__dot"></span>
      <span class="brand-mark__name">Fennel Cellar</span>
    </div>
  </section>

  <section class="card card--back" aria-label="Card back">
    <div class="brand-mark">
      <span class="brand-mark__dot"></span>
      <span class="brand-mark__name">Fennel Cellar</span>
    </div>
    <ul class="services">
      <li>Online store</li>
      <li>Cooking advice</li>
      <li>catering</li>
      <li>ristorante and</li>
      <li>information hub</li>
    </ul>
  </section>
</main>
</body>
</html>
```